Duct Manufacturing Company new to the industry needs business card and stationary design

we are sheet metal duct manufacturers looking for a business card design to fit my new business logo.
nothing to crazy that will date, but want it to stand out from the crowed.
I'm sure you guys will work it out.

Industry/Entity Type

Business

Contact Information for Business Card

Wade Collin
Director

Address
17 Paverly St
Tarrowgate NSW 2648

0438 657 904

Sales@flowbend.com.au

Font styles to use
Other font styles liked:
• BankGothic md bt

Requirements
Nice to have
• Like the idea of corner rounded to match logo
• like to keep colours flowing
• font I like sharp square not rounded

```html
<!DOCTYPE html>
<html lang="en">
<head>
<meta charset="utf-8">
<title>Flowbend Industries — Business Card</title>
<link href="https://fonts.googleapis.com/css2?family=Lato:wght@400;700;900&display=swap" rel="stylesheet">
<style>
  :root {
    --brand-blue: #024c99;
    --deep-blue: #0a3f86;
    --leaf-green: #8cc63f;
    --mid-green: #5aa32f;
    --paper: #efefef;
    --ink: #1f1f1f;
    --rule: #3a3a3a;
    --silver: #b9c4d3;
    --backdrop: #8e8d8e;
  }
  * { margin: 0; padding: 0; box-sizing: border-box; }
  html, body {
    width: 1200px; height: 900px; overflow: hidden;
    background: var(--backdrop);
    font-family: "Lato", Arial, sans-serif;
  }
  .stage { position: relative; width: 1200px; height: 900px; }
  .card {
    position: absolute; left: 250px; width: 700px; height: 400px;
    border-radius: 22px; overflow: hidden;
    box-shadow: 0 6px 18px rgba(0,0,0,.35);
  }
  .card--back { top: 40px; background: var(--brand-blue); }
  .card--front { top: 465px; }
  .card__shapes { position: absolute; inset: 0; }

  /* back */
  .back-brand {
    position: absolute; left: 0; right: 0; top: 125px;
    display: flex; flex-direction: column; align-items: center; gap: 8px;
  }
  .brand-mark {
    width: 54px; height: 54px; border-radius: 50%;
    background: var(--leaf-green);
  }
  .brand-name {
    font-weight: 900; font-size: 40px; letter-spacing: 3px;
    color: var(--leaf-green); text-transform: uppercase; line-height: 1.05;
    text-align: center;
  }
  .back-web {
    position: absolute; left: 60px; right: 60px; bottom: 52px;
    display: flex; align-items: center; gap: 16px;
    color: var(--silver); font-size: 17px; letter-spacing: .5px;
  }
  .back-web::before, .back-web::after {
    content: ""; flex: 1; height: 1px; background: var(--silver); opacity: .7;
  }

  /* front */
  .front-brand {
    position: absolute; left: 60px; top: 130px; width: 240px;
    display: flex; flex-direction: column; align-items: center; gap: 10px;
  }
  .front-brand .brand-name { font-size: 30px; color: var(--brand-blue); }
  .front-brand .brand-mark { background: var(--brand-blue); width: 46px; height: 46px; }
  .divider {
    position: absolute; left: 325px; top: 95px; width: 1px; height: 215px;
    background: var(--rule);
  }
  .contact { position: absolute; left: 350px; top: 100px; color: var(--ink); }
  .contact__name { font-weight: 900; font-size: 30px; color: var(--brand-blue); line-height: 1; }
  .contact__role { font-size: 18px; margin-top: 4px; margin-bottom: 16px; }
  .contact__row { display: flex; align-items: center; gap: 8px; font-size: 19px; line-height: 1.35; }
  .contact__row svg { width: 18px; height: 18px; flex: none; fill: var(--brand-blue); }
  .contact__row .accent { color: var(--brand-blue); }
  .contact__address { font-size: 19px; line-height: 1.3; margin-top: 14px; padding-left: 26px; }
</style>
</head>
<body>
<main class="stage">

  <section class="card card--back" aria-label="Card back">
    <div class="back-brand">
      <span class="brand-mark"></span>
      <span class="brand-name">Flowbend<br>Industries</span>
    </div>
    <div class="back-web">www.flowbend.com.au</div>
  </section>

  <section class="card card--front" aria-label="Card front">
    <svg class="card__shapes" viewBox="0 0 700 400" aria-hidden="true">
      <rect width="700" height="400" fill="var(--brand-blue)"/>
      <ellipse cx="360" cy="215" rx="385" ry="330" fill="var(--mid-green)"/>
      <ellipse cx="370" cy="215" rx="368" ry="318" fill="var(--leaf-green)"/>
      <ellipse cx="372" cy="218" rx="352" ry="312" fill="var(--paper)"/>
    </svg>

    <div class="front-brand">
      <span class="brand-mark"></span>
      <span class="brand-name">Flowbend<br>Industries</span>
    </div>

    <div class="divider"></div>

    <div class="contact">
      <div class="contact__name">Wade Collin</div>
      <div class="contact__role">Director</div>
      <div class="contact__row">
        <svg viewBox="0 0 24 24"><path d="M6.6 10.8a15.2 15.2 0 0 0 6.6 6.6l2.2-2.2c.3-.3.7-.4 1-.2 1.1.4 2.3.6 3.6.6.6 0 1 .4 1 1V20c0 .6-.4 1-1 1A17 17 0 0 1 3 4c0-.6.4-1 1-1h3.5c.6 0 1 .4 1 1 0 1.3.2 2.5.6 3.6.1.3 0 .7-.2 1z"/></svg>
        <span>0438 657 904</span>
      </div>
      <div class="contact__row">
        <svg viewBox="0 0 24 24"><path d="M2 5h20v14H2z M3.5 6.5 12 13l8.5-6.5" stroke="#fff" stroke-width="1.4"/></svg>
        <span>Sales@flowbend.com.au</span>
      </div>
      <div class="contact__row">
        <svg viewBox="0 0 24 24"><path d="M3 4h18v12H3zM5 6v8h14V6zM9 18h6v2H9z"/></svg>
        <span>www.<span class="accent">flowbend</span>.com.au</span>
      </div>
      <div class="contact__address">17 Paverly St<br>Tarrowgate NSW 2648</div>
    </div>
  </section>

</main>
</body>
</html>
```